Business Cards for new orthopaedic surgery practice

My husband and I are starting our own orthopaedic surgery practice. We are looking for a business card that is uniform, but one will have my name/title and the other will have his. You can just create one design with my name on it for now. But when I choose your design as the winning design I will ask that you add another copy with his name/title.

We are looking for classy, simple, elite all in one. We like dark blues/a little gold/yellow. Something that goes with our logo. We want our logo incorporated. Here is all the info you need:
Business name: RV Spine & Vitality Center
Location: 38915 North Bramble Ave
Palm Hollow, FL 33482
Phone: 954-218-4630
Fax: 954-571-2846
Email: info@myrvspine.example

Names: Lucinda Ferrow, M.D.
Board Certified Hand and Upper Extremity Surgeon

Emeka Dlunga, M.D.
Board Certified Hip & Knee Replacement/General Orthopaedic Surgeon

Can decide what you want to put on the back. Maybe a slogan:
Steady in Care. Centered on You

I am just going to upload our logo. The only thing is if we select you as the winning design, the location, and phone numbers may change. We will need your help to update that once fully solidified.

Industry/Entity Type

Medical

Contact Information for Business Card

Colors
0054AA
0677BA
7BADD7
CADEEF
E8F1F8
0094D4
00A9DD
6FCCEA
C7EBF8
E9F6FB

Requirements
Must have
• class, appeal,
Should not have
• We want to air on the side of masculine if we are looking at masculine vs. feminine feel. But we still want it classy, sophisticated, and something we will love

```html
<!DOCTYPE html>
<html lang="en">
<head>
<meta charset="utf-8">
<title>RV Spine &amp; Vitality Center — Business Card</title>
<link rel="stylesheet" href="https://fonts.googleapis.com/css2?family=Barlow:wght@400;600&display=swap">
<style>
  :root {
    --navy: #14234d;
    --navy-deep: #101d42;
    --gold: #b8964e;
    --paper: #f1f1f0;
    --strip: #e6e6e4;
    --backdrop: #d9d8d6;
    --ink-light: #e4e6ec;
  }
  * { margin: 0; padding: 0; box-sizing: border-box; }
  html, body { width: 1200px; height: 765px; overflow: hidden; }
  body {
    background: var(--backdrop);
    position: relative;
    font-family: "Barlow", sans-serif;
  }
  .card {
    position: absolute;
    width: 416px;
    height: 238px;
  }

  /* Front */
  .card-front {
    left: 285px; top: 129px;
    background: var(--paper);
  }
  .brand {
    position: absolute;
    left: 0; right: 0; top: 78px;
    display: flex; align-items: center; justify-content: center; gap: 10px;
  }
  .brand-dot {
    width: 14px; height: 14px; border-radius: 50%;
    background: var(--gold);
  }
  .brand-name {
    color: var(--navy);
    font-weight: 600;
    font-size: 21px;
    letter-spacing: 0.5px;
  }
  .tagline-band {
    position: absolute;
    left: 0; right: 0; top: 205px; height: 19px;
    background: var(--navy);
    color: var(--ink-light);
    font-size: 11.8px;
    letter-spacing: 0.6px;
    text-align: center;
    line-height: 19px;
  }

  /* Back */
  .card-back {
    left: 499px; top: 398px;
    background: linear-gradient(180deg, var(--navy) 0%, var(--navy-deep) 100%);
    color: var(--ink-light);
  }
  .accent-strip {
    position: absolute;
    left: 371px; top: 0; width: 18px; height: 211px;
    background: var(--strip);
  }
  .doctor-name {
    position: absolute; left: 28px; top: 21px;
    font-weight: 600; font-size: 18px; letter-spacing: 0.6px;
    color: #f2f3f6;
  }
  .doctor-title {
    position: absolute; left: 28px; top: 44px;
    font-size: 12.5px; line-height: 12.5px; letter-spacing: 0.3px;
  }
  .contact-list {
    position: absolute; left: 0; top: 133px; width: 389px;
    list-style: none;
  }
  .contact-item {
    height: 18px;
    display: flex; align-items: center; justify-content: flex-end;
    font-size: 12.2px; letter-spacing: 0.5px;
    white-space: nowrap;
  }
  .contact-item span { margin-right: 17px; }
  .contact-icon {
    width: 10px; height: 10px; margin-right: 4px;
    fill: var(--gold);
  }
</style>
</head>
<body>
  <section class="card card-front" aria-label="Card front">
    <div class="brand">
      <div class="brand-dot"></div>
      <div class="brand-name">RV Spine &amp; Vitality Center</div>
    </div>
    <div class="tagline-band">Steady in Care. Centered on You</div>
  </section>

  <section class="card card-back" aria-label="Card back">
    <div class="accent-strip"></div>
    <h1 class="doctor-name">LUCINDA FERROW, M.D.</h1>
    <p class="doctor-title">Board Certified Hand and<br>Upper Extremity Surgeon</p>
    <ul class="contact-list">
      <li class="contact-item"><span>954-218-4630</span>
        <svg class="contact-icon" viewBox="0 0 10 10" aria-hidden="true"><path d="M2 0.5 L3.6 2.6 L2.8 3.6 Q4 5.8 6.4 7.2 L7.4 6.4 L9.5 8 L8.4 9.5 Q4.5 9.3 1.6 5.6 Q0.4 3.6 0.6 1.6 Z"/></svg></li>
      <li class="contact-item"><span>954-571-2846</span>
        <svg class="contact-icon" viewBox="0 0 10 10" aria-hidden="true"><rect x="2.5" y="0.5" width="5" height="2.5"/><rect x="0.5" y="3.5" width="9" height="4"/><rect x="2.5" y="6.5" width="5" height="3"/></svg></li>
      <li class="contact-item"><span>info@myrvspine.example</span>
        <svg class="contact-icon" viewBox="0 0 10 10" aria-hidden="true" style="fill:none;stroke:var(--gold);stroke-width:1"><circle cx="5" cy="5" r="4.3"/><ellipse cx="5" cy="5" rx="1.9" ry="4.3"/><line x1="0.7" y1="5" x2="9.3" y2="5"/></svg></li>
      <li class="contact-item"><span>38915 North Bramble Ave Palm Hollow, FL 33482</span>
        <svg class="contact-icon" viewBox="0 0 10 10" aria-hidden="true"><path d="M5 0.3 A3.5 3.5 0 0 1 8.5 3.8 Q8.5 6 5 9.8 Q1.5 6 1.5 3.8 A3.5 3.5 0 0 1 5 0.3 Z M5 2.4 A1.4 1.4 0 1 0 5 5.2 A1.4 1.4 0 1 0 5 2.4 Z" fill-rule="evenodd"/></svg></li>
    </ul>
  </section>
</body>
</html>
```